Cuddle close with the brightest comet in your galaxy Zodiac handbook for finding deep romance and passion

I have had a graphic artist design a book cover which I am perfectly happy with. Unfortunately I've found that she sourced the image from the internet a year ago -- she says that the 90% of the image has been changed, but she hasn't responded to my request to see the original image, unchanged, so that I can be sure. Therefore, it's probably going to be a copyright problem. I have tried to attached the image she has created, which I have in dropbox and my photo library - but the file is huge. Please email me so that I can forward her email and the image on to you at marisolvendt@postvane.com.
Updates

I've had a request to supply a link for dropbox. I have the image in dropbox, but I'm unable to access the link, I'm not sure why. I also have it in iPhoto on my mac. If you are able to supply your email address I can send the iPhoto image to you. Thank you, Marisol Vendt Added Thursday, May 21, 2015

Target Market(s)

Love and sex - mostly women but written for both genders - adult market

Font styles to use
Decorative
Script

Requirements
Must have
• must be original - design must not reproduce, plagiarise or copy another's design. The file attached was submitted by a designer who copied it from the internet and 'cartooned' it so that it would look original, but it doesn't.
Nice to have
• I like the colour scheme in the attached file. the blue and orange text is a good combination, as it the black and white image - I would like a midnight blue background.

```html
<!DOCTYPE html>
<html lang="en">
<head>
<meta charset="utf-8">
<title>Cuddle Close – Book Cover</title>
<link rel="stylesheet" href="https://fonts.googleapis.com/css2?family=Cinzel:wght@400;500&display=swap">
<style>
  :root {
    --sky-top: #03060f;
    --sky-mid: #0c1f45;
    --sky-glow: #2a5aa0;
    --sky-horizon: #3f74b8;
    --hill-dark: #05080d;
    --hill-edge: #0e1621;
    --ink-light: #f4f6fb;
    --ink-soft: #e2e8f4;
    --rule: rgba(235, 240, 250, 0.85);
    --constellation: rgba(190, 210, 245, 0.28);
  }
  html, body {
    margin: 0;
    padding: 0;
    width: 800px;
    height: 1200px;
    overflow: hidden;
    background: var(--sky-top);
  }
  .cover {
    position: relative;
    width: 800px;
    height: 1200px;
    overflow: hidden;
    font-family: "Cinzel", "Trajan Pro", serif;
    color: var(--ink-light);
    background:
      radial-gradient(ellipse 70% 40% at 50% 80%, var(--sky-horizon) 0%, rgba(42,90,160,0.55) 35%, rgba(12,31,69,0) 75%),
      linear-gradient(180deg, var(--sky-top) 0%, #060d22 25%, var(--sky-mid) 55%, var(--sky-glow) 82%, var(--sky-horizon) 90%);
  }
  .starfield {
    position: absolute;
    inset: 0 0 200px 0;
    background: radial-gradient(ellipse at 50% 40%, rgba(150,180,230,0.10) 0%, rgba(150,180,230,0) 70%);
  }
  .zodiac-ring {
    position: absolute;
    left: 58px;
    top: 110px;
    width: 690px;
    height: 740px;
    border-radius: 50%;
    background: radial-gradient(ellipse at center,
      rgba(0,0,0,0) 50%,
      var(--constellation) 62%,
      rgba(220,230,250,0.18) 72%,
      rgba(0,0,0,0) 80%);
  }
  .hills {
    position: absolute;
    left: 0;
    bottom: 0;
    width: 800px;
    height: 240px;
  }
  .title-block {
    position: absolute;
    left: 0;
    top: 432px;
    width: 800px;
    text-align: center;
    text-shadow: 0 0 14px rgba(200, 220, 255, 0.55);
  }
  .title-main {
    margin: 0;
    font-weight: 400;
    font-size: 70px;
    line-height: 1;
    letter-spacing: 1px;
  }
  .title-tagline {
    margin: 10px 0 0;
    font-weight: 400;
    font-size: 29px;
    line-height: 36px;
    color: var(--ink-light);
  }
  .title-rule {
    width: 280px;
    height: 1px;
    margin: 16px auto 12px;
    background: var(--rule);
    border: 0;
  }
  .subtitle {
    margin: 0;
    font-size: 23px;
    line-height: 30px;
    color: var(--ink-soft);
  }
  .author {
    position: absolute;
    left: 0;
    top: 1072px;
    width: 800px;
    margin: 0;
    text-align: center;
    font-weight: 400;
    font-size: 62px;
    letter-spacing: 3px;
    color: var(--ink-light);
  }
</style>
</head>
<body>
  <main class="cover">
    <div class="starfield" role="img" aria-label="Night sky scattered with small stars"></div>
    <div class="zodiac-ring" role="img" aria-label="Ring of glowing zodiac constellation figures"></div>

    <svg class="hills" viewBox="0 0 800 240" role="img" aria-label="Dark silhouette of hills and trees on the horizon">
      <defs>
        <linearGradient id="hillShade" x1="0" y1="0" x2="0" y2="1">
          <stop offset="0" stop-color="var(--hill-edge)"/>
          <stop offset="0.4" stop-color="var(--hill-dark)"/>
          <stop offset="1" stop-color="var(--hill-dark)"/>
        </linearGradient>
      </defs>
      <path d="M0 70 C60 40 110 55 150 75 C220 95 300 80 380 88 C460 96 520 70 600 62 C680 55 740 70 800 80 L800 240 L0 240 Z" fill="url(#hillShade)"/>
    </svg>

    <header class="title-block">
      <h1 class="title-main">CUDDLE CLOSE</h1>
      <p class="title-tagline">With the brightest comet<br>in your galaxy</p>
      <hr class="title-rule">
      <p class="subtitle">Zodiac handbook<br>for finding deep<br>romance and passion</p>
    </header>

    <p class="author">COCO MARLOW</p>
  </main>
</body>
</html>
```